Christmas Sale banner ad for Watch Brand

I need a banner ad for a watch company running a christmas sale.
It should combine 3 models (images attached) and our logo. There are 2 images per model attached, feel free to choose either.
I have also added some photos with a clean background if needed.
The models are
Vantel (the one with disks for hands)
Plinto 2 (minimalist style shown in gold or white)
Brenn (jet plane themed photos)
The banner should have a black background. Text will be
Just in Time for Christmas - Up to 50% OFF!
Include a button for 'Shop Now'
Res should be 3000x2000
Men
It Company

```html
<!DOCTYPE html>
<html lang="en">
<head>
<meta charset="utf-8">
<title>Halden Christmas Sale Banner</title>
<link rel="stylesheet" href="https://fonts.googleapis.com/css2?family=Oswald:wght@500;600&display=swap">
<style>
  :root {
    --page: #ffffff;
    --banner: #000000;
    --white: #ffffff;
    --red: #e3202a;
    --steel: #3a3d42;
    --gold: #b98a62;
    --leather: #5a3b28;
    --glass: #c9ced4;
  }
  html, body {
    margin: 0;
    padding: 0;
    width: 1200px;
    height: 960px;
    overflow: hidden;
    background: var(--page);
  }
  .banner {
    position: absolute;
    left: 178px;
    top: 179px;
    width: 850px;
    height: 567px;
    background: var(--banner);
    overflow: hidden;
    font-family: 'Oswald', sans-serif;
    text-transform: uppercase;
  }
  .photo {
    position: absolute;
  }
  .photo-vantel {
    left: 490px; top: 52px; width: 342px; height: 128px;
    border-radius: 50%;
    background: radial-gradient(ellipse at 50% 45%, #eef0f2 0%, var(--glass) 45%, #5d6268 80%, #101214 100%);
  }
  .photo-brenn {
    left: 74px; top: 33px; width: 164px; height: 244px;
    border-radius: 40% 40% 30% 30%;
    background: radial-gradient(circle at 45% 45%, #2a2b2e 0%, #1b1c1e 40%, #3b3a32 70%, #0a0a0a 100%);
  }
  .photo-plinto-gold {
    left: 0; top: 236px; width: 194px; height: 328px;
    border-radius: 50%;
    background: radial-gradient(circle at 60% 52%, #14161b 0%, #14161b 26%, var(--gold) 32%, #2a2522 40%, #0b0b0b 70%, #000 100%);
  }
  .photo-plinto-white {
    left: 626px; top: 253px; width: 150px; height: 280px;
    border-radius: 50%;
    background: radial-gradient(circle at 50% 52%, #e4e4e0 0%, #d9d9d4 28%, var(--steel) 36%, var(--leather) 60%, #000 100%);
  }
  .photo-tree {
    left: 286px; top: 25px; width: 184px; height: 152px;
    border-radius: 8px;
    background: radial-gradient(ellipse at 50% 55%, #ffffff 0%, #f2dede 35%, rgba(255,255,255,0.15) 70%, rgba(0,0,0,0) 100%);
  }
  .headline {
    position: absolute;
    left: 0;
    top: 0;
    margin: 0;
    font-weight: 600;
    color: var(--white);
  }
  .line {
    position: absolute;
    left: 257px;
    display: block;
    line-height: 1;
    white-space: nowrap;
  }
  .line-just { top: 191px; font-size: 68px; letter-spacing: 0.5px; }
  .line-time { top: 265px; font-size: 55px; left: 260px; }
  .line-christmas { top: 327px; font-size: 71px; color: var(--red); }
  .line-offer { top: 406px; font-size: 52px; }
  .accent { color: var(--red); }
  .shop-button {
    position: absolute;
    left: 343px;
    top: 481px;
    width: 163px;
    height: 52px;
    box-sizing: border-box;
    background: var(--red);
    border: 3px solid var(--red);
    box-shadow: inset 0 0 0 2px var(--white);
    color: var(--white);
    font-size: 29px;
    font-weight: 500;
    line-height: 46px;
    text-align: center;
    text-decoration: none;
  }
  .brand {
    position: absolute;
    right: 14px;
    top: 500px;
    display: flex;
    align-items: center;
    gap: 6px;
    color: var(--white);
    font-size: 18px;
    font-weight: 500;
    line-height: 1;
    letter-spacing: 1px;
  }
  .brand-dot {
    width: 13px;
    height: 13px;
    border-radius: 50%;
    background: var(--white);
  }
</style>
</head>
<body>
  <section class="banner">
    <div class="photo photo-brenn" role="img" aria-label="Brenn automatic pilot watch in black with olive canvas strap"></div>
    <div class="photo photo-vantel" role="img" aria-label="Vantel watch with transparent case and disc hands"></div>
    <div class="photo photo-plinto-gold" role="img" aria-label="Plinto 2 watch with black dial, gold ring and black leather strap"></div>
    <div class="photo photo-plinto-white" role="img" aria-label="Plinto 2 watch with white dial and brown leather strap"></div>
    <div class="photo photo-tree" role="img" aria-label="White Christmas tree with red baubles and star, surrounded by snowflakes"></div>

    <h1 class="headline">
      <span class="line line-just">Just in</span>
      <span class="line line-time">Time for</span>
      <span class="line line-christmas">Christmas</span>
      <span class="line line-offer">Up to <span class="accent">50% off!</span></span>
    </h1>

    <a class="shop-button" href="#">Shop now</a>

    <div class="brand"><span class="brand-dot"></span>Halden</div>
  </section>
</body>
</html>
```